Cosmetics Brand Logo and Bottle Label Design

We are creating a new cosmetics brand called "Nolan Whitby" and would like you to create an amazing logo and bottle label for this brand's new 100% pure argan oil product.
For the logo, we really like the logo's of Marin Calloway and Vessa. The text should be Sans Serif (without feet).
For the actual bottle label, please find attached labels of one of our competitors design which really like. We really like the simplicity and elegance of the design. The only difference is that our product will be using light turqoise as the brand color. Please feel free to add your own creativity into it as well.
Industry/Entity Type
Cosmetics
Logo Text
Nolan Whitby
Font styles to use

```html
<!DOCTYPE html>
<html lang="en">
<head>
<meta charset="utf-8">
<title>Nolan Whitby – Label Design D01A</title>
<link rel="stylesheet" href="https://fonts.googleapis.com/css2?family=Source+Sans+3:wght@400;600;700&family=Quicksand:wght@600&family=Arimo&family=Pathway+Gothic+One&display=swap">
<style>
  :root {
    --board: #ffffff;
    --ink: #111111;
    --teal: #2a9d8f;
    --teal-soft: #a9d8d1;
    --label-fill: #e4f4f2;
    --label-edge: #bfe0db;
    --backdrop-light: #ffffff;
    --backdrop-dark: #d9d9d9;
  }
  * { margin: 0; padding: 0; box-sizing: border-box; }
  html, body { width: 1200px; height: 675px; overflow: hidden; background: var(--board); }
  .board { position: relative; width: 1200px; height: 675px; background: var(--board); color: var(--ink); font-family: "Source Sans 3", sans-serif; }

  .concept { position: absolute; left: 82px; top: 26px; width: 390px; }
  .concept-title { font-size: 21px; font-weight: 700; line-height: 1.3; }
  .concept-text { font-size: 19px; line-height: 25px; }

  .brand-mark { position: absolute; left: 470px; top: 78px; display: flex; align-items: center; gap: 10px; }
  .brand-mark-dot { width: 18px; height: 18px; border-radius: 50%; background: var(--teal); }
  .brand-mark-name { font-family: "Quicksand", sans-serif; font-weight: 600; font-size: 30px; color: var(--teal); }

  .label-heading { position: absolute; left: 82px; top: 224px; font-size: 24px; font-weight: 400; }

  .label { position: absolute; left: 82px; top: 270px; width: 611px; height: 369px; background: var(--label-fill); border: 2px solid var(--label-edge); border-radius: 28px; overflow: hidden; }
  .label-dot { position: absolute; left: 287px; top: 38px; width: 34px; height: 34px; border-radius: 50%; background: var(--teal-soft); }
  .label-band { position: absolute; top: 133px; height: 22px; background: var(--teal-soft); }
  .label-band--left { left: 0; width: 150px; background: linear-gradient(90deg, var(--label-fill), var(--teal-soft)); }
  .label-band--right { left: 460px; right: 0; background: linear-gradient(90deg, var(--teal-soft), var(--label-fill)); }
  .label-name { position: absolute; left: 150px; width: 310px; top: 118px; text-align: center; font-family: "Quicksand", sans-serif; font-weight: 600; font-size: 38px; letter-spacing: 1px; color: var(--teal); text-transform: uppercase; white-space: nowrap; }
  .label-product { position: absolute; left: 0; right: 0; top: 172px; text-align: center; font-family: "Arimo", sans-serif; font-size: 22px; padding-left: 20px; }
  .label-details { position: absolute; left: 346px; top: 262px; font-family: "Pathway Gothic One", sans-serif; font-size: 18px; line-height: 22px; }
  .label-volume { margin-top: 18px; font-size: 19px; }

  .backdrop { position: absolute; left: 805px; top: 0; width: 395px; height: 675px; background: radial-gradient(ellipse at 55% 45%, var(--backdrop-light) 30%, var(--backdrop-dark) 100%); }
</style>
</head>
<body>
<main class="board">
  <section class="concept">
    <h1 class="concept-title">Design Concept (D01)</h1>
    <p class="concept-text">Logo is a simple “NW” that stands for Nolan Whitby but is shaped to look like a “face” with the “N” as an eye and the “W” the right side of the face and the curve as the “chin”</p>
  </section>

  <div class="brand-mark">
    <span class="brand-mark-dot"></span>
    <span class="brand-mark-name">Nolan Whitby</span>
  </div>

  <h2 class="label-heading">Label Design D01A (Horizontal Layout)</h2>

  <section class="label">
    <span class="label-dot"></span>
    <span class="label-band label-band--left"></span>
    <span class="label-band label-band--right"></span>
    <p class="label-name">Nolan Whitby</p>
    <p class="label-product">100% Pure Argan Oil</p>
    <div class="label-details">
      <p>organic<br>moisturizing oil</p>
      <p class="label-volume">50 mL 1.7 fl.oz</p>
    </div>
  </section>

  <div class="backdrop"></div>
</main>
</body>
</html>
```